Velko
trosen
Use same font as used in my logo
Yousef Harbi يوسف حربي
General manager المدير العام
P.O.Box 48735 Riyadh 13542
Saudi Arabia
ص.ب 48735 الرياض 13542
المملكة العربية السعودية
Info@velkohouse.example
www.velkohouse.example
C.R. 1049728513 CC.487139
I want to be design Arabic & English

```html
<!DOCTYPE html>
<html lang="en">
<head>
<meta charset="utf-8">
<title>Velko House — Business Card</title>
<link rel="stylesheet" href="https://fonts.googleapis.com/css2?family=Cairo:wght@400;600;700&family=Cinzel:wght@700&family=Open+Sans:wght@400;600;700&display=swap">
<style>
  :root {
    --brand-blue: #3b6eae;
    --ink-grey: #5b5f66;
    --paper: #ffffff;
    --backdrop: #e9ebee;
    --rule: #b9c3d1;
  }
  * { box-sizing: border-box; margin: 0; padding: 0; }
  html, body { width: 1200px; height: 864px; overflow: hidden; }
  body {
    background: var(--backdrop);
    font-family: "Open Sans", Arial, sans-serif;
    position: relative;
  }
  .card {
    position: absolute;
    width: 640px;
    height: 365px;
    border-radius: 22px;
    overflow: hidden;
    box-shadow: 0 6px 18px rgba(0,0,0,0.18);
  }
  /* Back side */
  .card--back {
    left: 90px; top: 45px;
    background: var(--brand-blue);
    display: flex; flex-direction: column; align-items: center; justify-content: center;
    gap: 26px;
  }
  .back-mark {
    display: flex; align-items: center; gap: 14px;
    color: var(--paper);
    font-family: "Cinzel", Georgia, serif;
    font-weight: 700; font-size: 46px; letter-spacing: 2px;
  }
  .mark-dot { border-radius: 50%; flex: none; }
  .back-mark .mark-dot { width: 52px; height: 52px; background: var(--paper); }
  .back-web { color: var(--paper); font-size: 14px; letter-spacing: 4px; }
  /* Front side */
  .card--front {
    left: 470px; top: 454px;
    background: var(--paper);
  }
  .swoosh { position: absolute; right: 0; top: 0; width: 140px; height: 365px; }
  .front-brand {
    position: absolute; left: 44px; top: 44px;
    display: flex; align-items: center; gap: 18px;
  }
  .front-brand .mark-dot { width: 64px; height: 64px; background: var(--brand-blue); }
  .front-brand .brand-name {
    font-family: "Cinzel", Georgia, serif; font-weight: 700;
    font-size: 44px; color: var(--brand-blue); letter-spacing: 1px;
  }
  .person {
    position: absolute; left: 48px; top: 160px; width: 222px;
    color: var(--ink-grey);
  }
  .person .row { display: flex; justify-content: space-between; align-items: baseline; }
  .ar { font-family: "Cairo", "Open Sans", sans-serif; direction: rtl; }
  .person .person-name { color: var(--brand-blue); font-weight: 700; font-size: 19px; line-height: 26px; }
  .person .person-name-ar { color: var(--brand-blue); font-weight: 700; font-size: 15px; }
  .person .person-role { font-size: 13px; line-height: 20px; }
  .person .person-role-ar { font-size: 13px; }
  .person .person-address { font-size: 12px; margin-top: 10px; line-height: 17px; }
  .person .person-address-ar { font-size: 12px; line-height: 19px; text-align: left; margin-top: 2px; }
  .person .person-reg { font-size: 11.5px; margin-top: 6px; line-height: 17px; }
  .divider {
    position: absolute; left: 284px; top: 166px; width: 1.5px; height: 148px;
    background: var(--rule);
  }
  .contacts {
    position: absolute; left: 302px; top: 168px; list-style: none;
    color: var(--ink-grey); font-size: 13px;
  }
  .contacts li { display: flex; align-items: center; gap: 9px; height: 28px; }
  .contacts svg { width: 18px; height: 18px; flex: none; }
</style>
</head>
<body>

<section class="card card--back">
  <div class="back-mark"><span class="mark-dot"></span>Velko</div>
  <p class="back-web">www.velkohouse.example</p>
</section>

<section class="card card--front">
  <svg class="swoosh" viewBox="0 0 140 365" aria-hidden="true">
    <path d="M140 0 L110 0 C60 90 60 260 104 365 L140 365 Z" fill="var(--brand-blue)"/>
    <path d="M88 0 C38 100 40 260 84 365" fill="none" stroke="var(--brand-blue)" stroke-width="4"/>
  </svg>

  <div class="front-brand">
    <span class="mark-dot"></span>
    <span class="brand-name">VELKO HOUSE</span>
  </div>

  <div class="person">
    <div class="row">
      <p class="person-name">Yousef Harbi</p>
      <p class="person-name-ar ar" lang="ar">يوسف حربي</p>
    </div>
    <div class="row">
      <p class="person-role">General manager</p>
      <p class="person-role-ar ar" lang="ar">المدير العام</p>
    </div>
    <p class="person-address">P.O.Box 48735 Riyadh 13542<br>Saudi Arabia</p>
    <p class="person-address-ar ar" lang="ar">ص.ب 48735 الرياض 13542<br>المملكة العربية السعودية</p>
    <p class="person-reg">C.R. 1049728513 &nbsp;CC.487139</p>
  </div>

  <div class="divider"></div>

  <ul class="contacts">
    <li>
      <svg viewBox="0 0 18 18"><circle cx="9" cy="9" r="9" fill="var(--brand-blue)"/><path d="M6 4.5l1.8 0 .8 2.3-1.1.9c.6 1.3 1.5 2.2 2.8 2.8l.9-1.1 2.3.8v1.8c0 .6-.5 1-1.1 1C8.4 13.7 4.3 9.6 4.9 5.6 5 5 5.4 4.5 6 4.5z" fill="#fff"/></svg>
      +966550187624
    </li>
    <li>
      <svg viewBox="0 0 18 18"><circle cx="9" cy="9" r="9" fill="var(--brand-blue)"/><path d="M6 4.5l1.8 0 .8 2.3-1.1.9c.6 1.3 1.5 2.2 2.8 2.8l.9-1.1 2.3.8v1.8c0 .6-.5 1-1.1 1C8.4 13.7 4.3 9.6 4.9 5.6 5 5 5.4 4.5 6 4.5z" fill="#fff"/></svg>
      +966114870352
    </li>
    <li>
      <svg viewBox="0 0 18 18"><circle cx="9" cy="9" r="9" fill="var(--brand-blue)"/><rect x="5" y="7" width="8" height="5" rx="1" fill="#fff"/><rect x="6.5" y="4.5" width="5" height="3" fill="#fff"/></svg>
      +966114870353
    </li>
    <li>
      <svg viewBox="0 0 18 18"><circle cx="9" cy="9" r="9" fill="var(--brand-blue)"/><rect x="4.5" y="5.5" width="9" height="7" rx="1" fill="#fff"/><path d="M4.8 6l4.2 3.5L13.2 6" fill="none" stroke="var(--brand-blue)" stroke-width="1"/></svg>
      Info@velkohouse.example
    </li>
    <li>
      <svg viewBox="0 0 18 18"><circle cx="9" cy="9" r="9" fill="var(--brand-blue)"/><circle cx="9" cy="9" r="4.5" fill="none" stroke="#fff" stroke-width="1.2"/><path d="M4.5 9h9M9 4.5c-2 2.5-2 6.5 0 9M9 4.5c2 2.5 2 6.5 0 9" fill="none" stroke="#fff" stroke-width="1"/></svg>
      www.velkohouse.example
    </li>
  </ul>
</section>

</body>
</html>
```